Christmas Card Design for Trevindle Project Management Ltd

Trevindle Project Management Ltd is a start up business in the construction project management field and we have been working hard this year at makin...

Target Market(s)

The main receivers of this card will be male and either in CEO positions within companies or workers in the construction industry.

Industry/Entity Type

Construction

Requirements
Must have
• The design dimensions should fit on a card to be printed of 18.2 x 11.7 cm Folded.
• Please ensure the card design agrees with the logos uploaded and incorporate the trevindle bird.
Nice to have
• Christmas in New Zealand is summer time and our holiday festive season includes sun, beaches, barbecues, beer, family time.
• Reference to large scale construction picture/design (say sports facility or school building)

```html
<!DOCTYPE html>
<html lang="en">
<head>
<meta charset="utf-8">
<title>Trevindle Project Management – Christmas Card</title>
<link href="https://fonts.googleapis.com/css2?family=Lato:wght@400;700&display=swap" rel="stylesheet">
<style>
  :root {
    --backdrop: #e2e2e2;
    --paper: #ffffff;
    --brand-blue: #3478b8;
    --brand-orange: #f5a03a;
    --ink-grey: #6a6a6a;
    --label-ink: #333333;
    --sky-top: #3f7fd0;
    --sea: #3fb8c8;
    --sand: #ece8e2;
  }
  * { margin: 0; padding: 0; box-sizing: border-box; }
  html, body { width: 1200px; height: 900px; overflow: hidden; }
  body {
    background: var(--backdrop);
    font-family: 'Lato', sans-serif;
    position: relative;
  }
  .spread-label {
    position: absolute;
    left: 0; width: 1200px;
    text-align: center;
    font-size: 12.5px;
    color: var(--label-ink);
  }
  .spread-label--outside { top: 65px; }
  .spread-label--inside { top: 811px; }

  .spread {
    position: absolute;
    left: 65px;
    width: 1070px;
    display: flex;
    box-shadow: 0 4px 12px rgba(0,0,0,0.35);
  }
  .spread--outside { top: 106px; height: 339px; }
  .spread--inside { top: 468px; height: 324px; }

  .panel { position: relative; height: 100%; }
  .panel--back { width: 537px; background: var(--paper); }
  .panel--front {
    flex: 1;
    background: linear-gradient(180deg,
      #2f6fc4 0%, #6fa3dc 14%, #9cc7e8 22%,
      #2c9bc0 24%, var(--sea) 30%, #bfe3e4 36%,
      #e6e8e6 42%, var(--sand) 100%);
  }
  .panel--greeting {
    width: 536px;
    background: var(--brand-blue);
    display: flex; align-items: center; justify-content: center;
  }
  .panel--closing {
    flex: 1;
    background: var(--paper);
    display: flex; align-items: center; justify-content: center;
  }

  .brand-name {
    position: absolute;
    left: 128px; top: 322px;
    width: 112px;
  }
  .contact-block {
    position: absolute;
    left: 245px; top: 192px;
    height: 91px;
    padding-left: 16px;
    border-left: 1.5px solid var(--brand-orange);
  }
  .brand-name {
    left: 128px; top: 220px;
    text-align: center;
    font-weight: 700;
    font-size: 10.5px;
    line-height: 1.25;
    color: var(--brand-blue);
  }
  .contact-name {
    font-size: 14.5px;
    color: var(--ink-grey);
    margin-top: -2px;
  }
  .contact-credentials, .contact-role {
    font-size: 7px;
    letter-spacing: 0.6px;
    color: var(--ink-grey);
    line-height: 1.35;
  }
  .contact-list { list-style: none; margin-top: 9px; }
  .contact-list li {
    display: flex; align-items: center; gap: 5px;
    font-size: 6.5px;
    letter-spacing: 0.4px;
    color: var(--ink-grey);
    height: 18px;
  }
  .contact-icon { width: 10px; height: 10px; flex: none; }

  .greeting-text {
    font-size: 13.5px;
    color: var(--paper);
  }
  .closing-line { display: flex; align-items: center; gap: 10px; }
  .closing-brand {
    display: flex; align-items: center; gap: 5px;
    font-size: 13.5px; color: var(--brand-blue);
  }
  .closing-brand-dot {
    width: 10px; height: 10px; border-radius: 50%;
    background: var(--brand-blue);
  }
  .closing-text { font-size: 13.5px; color: var(--brand-orange); }
</style>
</head>
<body>
  <p class="spread-label spread-label--outside">Outside</p>

  <section class="spread spread--outside">
    <div class="panel panel--back">
      <p class="brand-name">TREVINDLE PROJECT MANAGEMENT</p>
      <div class="contact-block">
        <p class="contact-name">Graham Whitfield</p>
        <p class="contact-credentials">(PMP, PMINZ)</p>
        <p class="contact-role">Director</p>
        <ul class="contact-list">
          <li>
            <svg class="contact-icon" viewBox="0 0 10 10"><rect x="0.5" y="0.5" width="9" height="9" fill="none" stroke="#f5a03a"/><path d="M3 2.5 L4.2 2.5 L4.6 4 L3.9 4.6 Q4.6 6 5.6 6.3 L6.2 5.6 L7.5 6.1 L7.5 7.3 Q4.5 7.5 3 2.5Z" fill="#f5a03a"/></svg>
            021555019
          </li>
          <li>
            <svg class="contact-icon" viewBox="0 0 10 10"><rect width="10" height="10" fill="#f5a03a"/><path d="M2 3 H8 V7 H2 Z M2 3 L5 5.3 L8 3" fill="none" stroke="#fff" stroke-width="0.8"/></svg>
            graham@trevindlepm.co.nz
          </li>
          <li>
            <svg class="contact-icon" viewBox="0 0 10 10"><rect width="10" height="10" fill="#f5a03a"/><circle cx="5" cy="5" r="3" fill="none" stroke="#fff" stroke-width="0.8"/><path d="M2 5 H8 M5 2 V8" stroke="#fff" stroke-width="0.6"/></svg>
            www.trevindleprojectmanagement.co.nz
          </li>
        </ul>
      </div>
    </div>
    <div class="panel panel--front" role="img" aria-label="Photo of a sunny New Zealand beach with turquoise surf and a red Santa hat resting on white sand"></div>
  </section>

  <section class="spread spread--inside">
    <div class="panel panel--greeting">
      <p class="greeting-text">Wishing you a great festive season and a prosperous new year.</p>
    </div>
    <div class="panel panel--closing">
      <div class="closing-line">
        <span class="closing-brand"><span class="closing-brand-dot"></span>Trevindle</span>
        <p class="closing-text">We look forward to working with you in the future.</p>
      </div>
    </div>
  </section>

  <p class="spread-label spread-label--inside">Inside</p>
</body>
</html>
```